依頼概要
■依頼の目的/概要
母の日用新品種アジサイの販促ポスターの作成依頼です。

■依頼詳細
・ポスターサイズはA2を予定しています。
・ターゲット
大人可愛い、北欧系のインテリアやおしゃれなライフスタイルを好む30代女性
・テーマ、カラー
ナチュラル系、淡めの暖色系、おしゃれなカフェや雑貨屋さんに合うような雰囲気
※実際にはポスターを貼って頂くところは花屋さんですが、花を買ったことがない人にも興味を持って頂くのが狙いです。

補足情報は添付ファイルをご確認ください。

細かい所はやり取りしながら相談させて頂きたいと思います。
よろしくお願いいたします。
■ 選んだ理由

素敵で可愛らしいデザインがいくつもあり迷いましたが、
私達の目指すコンセプトやターゲットに当てはまるデザイン案を
選ばせていただきました。

■ 提案者全員のお礼・コメント

ご提案くださったランサーの皆さまへ

予想以上にたくさんのご提案をいただき、大変有難く思っております。
このアジサイは私達にとって、とても大切な品種で思い入れがあります。

最終決定するまで、随分迷いました。
素敵なデザインをご提案くださった皆さまにこの場を借りて感謝申し上げます。
有難うございました。

また機会がありましたら、その際はよろしくお願い致します。

```html
<!DOCTYPE html>
<html lang="ja">
<head>
<meta charset="utf-8">
<title>紅霞 — 母に捧ぐ アジサイ浪漫</title>
<link rel="stylesheet" href="https://fonts.googleapis.com/css2?family=Cormorant+Garamond:wght@500&family=Shippori+Mincho:wght@400;500;600&display=swap">
<style>
  :root {
    --paper: #ffffff;
    --rose: #e58a9f;
    --rose-deep: #d96f88;
    --rose-soft: #f6cdd7;
    --blush: #fbe6ec;
    --leaf: #b9d79a;
    --leaf-soft: #e4efd6;
    --ink-muted: #9a8f93;
  }
  html, body {
    margin: 0;
    padding: 0;
    overflow: hidden;
    background: var(--paper);
  }
  .poster {
    position: relative;
    width: 851px;
    height: 1200px;
    overflow: hidden;
    background: var(--paper);
    font-family: "Shippori Mincho", serif;
  }
  .flower-visual {
    position: absolute;
    left: 30px;
    top: 100px;
    width: 520px;
    height: 850px;
    border-radius: 50%;
    background: radial-gradient(ellipse at 52% 47%,
      var(--rose-soft) 0%, var(--blush) 38%, var(--leaf-soft) 58%, rgba(255,255,255,0) 72%);
  }
  .petals-top {
    position: absolute;
    right: 0;
    top: 0;
    width: 280px;
    height: 180px;
    background: radial-gradient(ellipse at 80% 20%, var(--blush) 0%, rgba(255,255,255,0) 65%);
  }
  .petals-bottom {
    position: absolute;
    left: 0;
    bottom: 60px;
    width: 420px;
    height: 260px;
    background: radial-gradient(ellipse at 35% 60%, var(--blush) 0%, rgba(255,255,255,0) 65%);
  }
  .vertical {
    position: absolute;
    writing-mode: vertical-rl;
    margin: 0;
    color: var(--rose);
  }
  .name-latin {
    left: 72px;
    top: 52px;
    font-family: "Cormorant Garamond", serif;
    font-size: 24px;
    letter-spacing: 0.22em;
    font-weight: 500;
  }
  .tagline {
    left: 100px;
    top: 575px;
    font-size: 27px;
    letter-spacing: 0.12em;
    font-weight: 500;
  }
  .origin {
    left: 652px;
    top: 140px;
    font-family: "Cormorant Garamond", serif;
    font-size: 16px;
    letter-spacing: 0.16em;
    color: var(--rose-deep);
  }
  .title {
    left: 545px;
    top: 410px;
    font-size: 290px;
    line-height: 1;
    font-weight: 500;
    letter-spacing: 0.04em;
    color: var(--rose);
  }
  .footer {
    position: absolute;
    right: 16px;
    bottom: 34px;
    display: flex;
    align-items: center;
    gap: 10px;
    white-space: nowrap;
  }
  .footer-club {
    font-family: "Cormorant Garamond", serif;
    font-size: 11px;
    color: var(--ink-muted);
  }
  .footer-org {
    font-size: 19px;
    font-weight: 600;
    color: var(--rose-deep);
    letter-spacing: 0.04em;
  }
  .footer-tag {
    background: var(--rose);
    color: var(--paper);
    font-size: 9px;
    padding: 2px 6px;
  }
  .footer-url {
    font-family: "Cormorant Garamond", serif;
    font-size: 10px;
    color: var(--ink-muted);
  }
</style>
</head>
<body>
  <main class="poster">
    <div class="petals-top" role="img" aria-label="淡いピンクの花びらが舞う様子"></div>
    <div class="petals-bottom" role="img" aria-label="足元に散るピンクの花びら"></div>
    <div class="flower-visual" role="img" aria-label="緑の葉を添えたピンクのアジサイの花房の写真"></div>

    <p class="vertical name-latin">BENIGASUMI</p>
    <p class="vertical tagline">母に捧ぐ　アジサイ浪漫</p>
    <p class="vertical origin">IZUMO ORIGINAL</p>
    <h1 class="vertical title">紅霞</h1>

    <footer class="footer">
      <span class="footer-club">Izumo Hanazono Club</span>
      <span class="footer-org">出雲花苑アジサイ会</span>
      <span class="footer-tag">公式</span>
      <span class="footer-url">www.izumo-ajisai.jp</span>
    </footer>
  </main>
</body>
</html>
```